Accounting Firm

We are a two partner accounting firm. our business name is BELLWOOD & TRASK. We are accountants and business consultants.

We need a stationery design for our letterhead, with compliments slip, business card and envelope.

We'd like clean, professional look. I'm 39 years old and my partner is 60+, so we'd like modern yet elegant design. Dark Navy Blue as a primary colour is preferred.

Thank you.
Updates

Hi Guys

No logo.

Thanks

Industry/Entity Type

Accounting

Requirements
Must have
• Firm name :BELLWOOD & TRASK
Business Consultants & Accountants
Address: Level 2 Units 3 & 4, 17 Merrow Crescent DALEFORD SA 5099
Box address: PO Box 418 ASHGROVE SA 5098
telp: +61 8 8555 0142
fax: +61 8 8555 0187

Martin Bellwood, CA
Lucas Trask, CPA

martin.bellwood@bellwoodtrask.example.com.au
lucas.trask@bellwoodtrask.example.com.au

Dark Navy Blue as primary colour

```html
<!DOCTYPE html>
<html lang="en">
<head>
<meta charset="utf-8">
<title>Bellwood &amp; Trask — Letterhead: Front and back</title>
<link rel="stylesheet" href="https://fonts.googleapis.com/css2?family=Questrial&family=Nunito+Sans:wght@700&display=swap">
<style>
  :root {
    --navy: #020080;
    --brand-blue: #1a1aa6;
    --ink-grey: #8a8a8a;
    --label-grey: #7a7a7a;
    --frame-grey: #bdbdbd;
    --paper: #ffffff;
    --caption: #111111;
  }
  * { margin: 0; padding: 0; box-sizing: border-box; }
  html, body {
    width: 1200px; height: 900px; overflow: hidden;
    background: var(--paper);
  }
  .canvas { position: relative; width: 1200px; height: 900px; }

  .sheet-caption {
    position: absolute; left: 16px; top: 41px;
    font-family: "Nunito Sans", sans-serif; font-weight: 700;
    font-size: 11px; color: var(--caption);
  }

  .sheet { position: absolute; top: 81px; width: 507px; height: 717px; }
  .sheet--front { left: 65px; border: 1px solid var(--frame-grey); background: var(--paper); }
  .sheet--back { left: 627px; background: var(--navy); }

  .letter-header { position: absolute; left: 35px; top: 26px; }
  .firm-name {
    font-family: "Questrial", sans-serif; font-weight: 400;
    font-size: 14px; letter-spacing: 1px; line-height: 18px;
    color: var(--navy); white-space: nowrap;
  }
  .firm-services {
    margin-top: 4px;
    font-family: "Questrial", sans-serif; font-size: 8px;
    line-height: 12px; color: var(--ink-grey); white-space: nowrap;
  }

  .contact-block {
    position: absolute; right: 34px; top: 495px;
    display: flex; flex-direction: column; align-items: flex-end;
    text-align: right; font-style: normal;
    font-family: "Questrial", sans-serif; font-size: 6.6px;
    line-height: 12px; color: var(--ink-grey);
  }
  .contact-line { display: block; white-space: nowrap; }
  .contact-label {
    font-family: "Nunito Sans", sans-serif; font-weight: 700;
    color: var(--label-grey);
  }
  .contact-divider { display: block; width: 64px; height: 12px; }
  .contact-divider line {
    stroke: var(--brand-blue); stroke-width: 1.6;
    stroke-linecap: round; stroke-dasharray: 0 3.2;
  }
</style>
</head>
<body>
<div class="canvas">
  <p class="sheet-caption">Letterhead: Front and back</p>

  <section class="sheet sheet--front" aria-label="Letterhead front">
    <header class="letter-header">
      <h1 class="firm-name">BELLWOOD &amp; TRASK</h1>
      <p class="firm-services">Business Consultants &amp; Accountants</p>
    </header>

    <address class="contact-block">
      <span class="contact-line contact-label">Address</span>
      <span class="contact-line">Level 2 Units 3 &amp; 4,</span>
      <span class="contact-line">17 Merrow Crescent</span>
      <span class="contact-line">Daleford</span>
      <span class="contact-line">SA 5099</span>
      <svg class="contact-divider" viewBox="0 0 64 12" aria-hidden="true"><line x1="1" y1="6" x2="63" y2="6"/></svg>
      <span class="contact-line contact-label">Box address</span>
      <span class="contact-line">PO Box 418</span>
      <span class="contact-line">Ashgrove</span>
      <span class="contact-line">SA 5098</span>
      <svg class="contact-divider" viewBox="0 0 64 12" aria-hidden="true"><line x1="1" y1="6" x2="63" y2="6"/></svg>
      <span class="contact-line">T: +61 8 8555 0142</span>
      <span class="contact-line">F: +61 8 8555 0187</span>
      <svg class="contact-divider" viewBox="0 0 64 12" aria-hidden="true"><line x1="1" y1="6" x2="63" y2="6"/></svg>
      <span class="contact-line">martin.bellwood@bellwoodtrask.example.com.au</span>
      <span class="contact-line">lucas.trask@bellwoodtrask.example.com.au</span>
    </address>
  </section>

  <section class="sheet sheet--back" aria-label="Letterhead back"></section>
</div>
</body>
</html>
```